Need a business card for our overland brand!

We had the logo made and we need a great design for our business card. Use the logo provide or tweak it however you see fit.

Contact Information for Business Card

Name, Title, Telephone, email, website

```html
<!DOCTYPE html>
<html lang="en">
<head>
<meta charset="utf-8">
<title>Peakline Overland – Business Card</title>
<link rel="stylesheet" href="https://fonts.googleapis.com/css2?family=Arimo:wght@400;700&display=swap">
<style>
  :root {
    --navy: #253a52;
    --cyan: #1ba0cc;
    --sky: #2bb4e8;
    --white: #ffffff;
    --ink: #1c2633;
    --backdrop: #ece9e4;
  }
  * { box-sizing: border-box; margin: 0; padding: 0; }
  html, body {
    width: 1200px; height: 1023px; overflow: hidden;
    background: var(--backdrop);
    font-family: "Arimo", Arial, sans-serif;
  }
  .card {
    position: absolute;
    width: 580px; height: 330px;
    border-radius: 22px;
    overflow: hidden;
    box-shadow: 0 10px 28px rgba(0,0,0,0.18);
  }
  .card-back {
    left: 70px; top: 90px;
    background: var(--navy);
    display: flex; align-items: center; justify-content: center;
  }
  .brand-name {
    font-family: "Arimo", Arial, sans-serif;
    font-weight: 700;
    text-transform: uppercase;
    line-height: 0.95;
    text-align: center;
    letter-spacing: 1px;
  }
  .card-back .brand-name { color: var(--white); font-size: 64px; }
  .card-front { left: 550px; top: 600px; background: var(--white); }
  .wave { position: absolute; inset: 0; }
  .card-front .brand-name {
    position: absolute; left: 40px; top: 112px; width: 210px;
    color: var(--navy); font-size: 38px;
  }
  .divider {
    position: absolute; left: 270px; top: 48px;
    width: 2px; height: 156px; background: var(--cyan);
  }
  .contact { position: absolute; left: 292px; top: 36px; color: var(--ink); }
  .person-name { font-size: 30px; line-height: 1.15; font-weight: 700; color: var(--navy); letter-spacing: 0.3px; }
  .person-name .first { color: var(--sky); }
  .person-title { font-size: 13px; line-height: 1.3; margin-top: 2px; }
  .address { font-size: 13px; line-height: 1.3; margin-top: 10px; }
  .links { list-style: none; margin-top: 8px; font-size: 13px; }
  .links li { display: flex; align-items: center; gap: 8px; line-height: 1.45; }
  .links svg { width: 13px; height: 13px; flex: none; }
</style>
</head>
<body>

<section class="card card-back">
  <div class="brand-name">Peakline<br>Overland</div>
</section>

<section class="card card-front">
  <svg class="wave" viewBox="0 0 580 330" preserveAspectRatio="none" aria-hidden="true">
    <path d="M0,314 C200,290 330,266 430,238 C500,218 550,190 580,145 L580,330 L0,330 Z" fill="var(--navy)"/>
    <path d="M0,314 C200,290 330,266 430,238 C500,218 550,190 580,145" fill="none" stroke="var(--cyan)" stroke-width="5"/>
  </svg>

  <div class="brand-name">Peakline<br>Overland</div>
  <div class="divider"></div>

  <div class="contact">
    <h1 class="person-name"><span class="first">Dana</span> Rowe</h1>
    <p class="person-title">Managing Director</p>
    <p class="address">420 Alder Ridge Rd, Ste 12,<br>Boulder, CO 80302</p>
    <ul class="links">
      <li>
        <svg viewBox="0 0 16 16"><path fill="var(--cyan)" d="M3 1l3 3-2 2c1 2 3 4 5 5l2-2 3 3-2 3C7 15 1 9 1 3z"/></svg>
        800-555-0142
      </li>
      <li>
        <svg viewBox="0 0 16 16"><rect x="1" y="3" width="14" height="10" rx="1" fill="var(--cyan)"/><path d="M1 4l7 5 7-5" fill="none" stroke="#fff" stroke-width="1.4"/></svg>
        hello@peakline-mail.com
      </li>
      <li>
        <svg viewBox="0 0 16 16"><circle cx="8" cy="8" r="7" fill="var(--cyan)"/><path d="M1 8h14M8 1c3 3 3 11 0 14M8 1c-3 3-3 11 0 14" fill="none" stroke="#fff" stroke-width="1"/></svg>
        www.peakline-web.com
      </li>
    </ul>
  </div>
</section>

</body>
</html>
```